New Design for Accounting Firm

CLIENT NAME: Corvantel
CURRENT WEBSITE: www.corvantelgroup.com.au

CLIENTS THE CLIENT LIKES:
http://vetrulka.se/
http://www.markoplex.biz/index.php
http://www.frendaworks.co.uk/
http://www.brightharbourrelief.org/

COLOUR THEMES:
Colour theme to reflect the logo, with a leaning to blue in Accounting & Audit sections and green in Super section.

LOOK AND FEEL:
The look and feel needs to reflect an accessible culture and contemporary sensibility while still communicating our experience and stability as a professional company.

ABOUT:
The concept of 'Corvantel' is integral to our identity. Definition: 'The connection of creative ideas from a group of diverse individuals, applied with the end aim of solving practical problems'. See ''About Us'' on our website for more.

OTHER DETAILS:
Our three divisions (and service areas within each division) must be easily navigated as they related to very different users of the site. Two client sign in sections (Accounting & Super) must be easily distinguished to avoid user confusion.

MENU STRUCTURE:
* About
- includes history, values, our people, community etc
* Accounting & Advisory
- About
- Services
- Tax & Accounting
- Business Advisory
- Family Wealth Management
- Client Sign In
- Calculators
* Audit & Assurance
- About
- Services
* Corvantel Super
- About
- Individuals
- Services
- Advisers
- Services
- Portal Sign In
- Calculators
* Careers
* Newsletters
* Contact

REQUIREMENTS:
- Layered PSD form home and content pages
- No coding required, we use our own CMS to insert XHTML files into.
Updates

Hi Guys,

The client has asked for a non-cliche'd images in the design. If you'd like to try again with some images that represent the business but aren't your standard boring accounting-looking people, then please do! Cliche is a killer in design - please pump some creativity in!

Cheers,
Ned.

Reason: GUYS - PLEASE LISTEN TO THESE COMMENTS - I'VE SAID THEM TWICE NOW AND PEOPLE ARE STILL POSTING PROJECTS WITH CLICHED AND OBVIOUS ACCOUTNING TYPE IMAGES. USE YOUR CREATIVITY AND POST A DESIGN THAT IS OUTSIDE THE BOX WITH REGARDS TO THE IMAGES YOU ARE USING.

Reason: I am waiting to hear back from the client on their decision.

```html
<!DOCTYPE html>
<html lang="en">
<head>
<meta charset="utf-8">
<title>Corvantel Group – Accounting, Audit and Super</title>
<link rel="stylesheet" href="https://fonts.googleapis.com/css2?family=Arimo:wght@400;700&family=PT+Sans:wght@400;700&display=swap">
<style>
:root{
  --page:#373b3f;
  --blue:#1a63a8;
  --blue-dark:#0f4c86;
  --ink:#333;
  --ink-soft:#555;
  --panel:#efefef;
  --header:#f0eff2;
  --dark:#1f2022;
  --darker:#161718;
  --field:#1c1d1f;
  --line:#c9c9c9;
  --yellow:#f7c21a;
}
*{box-sizing:border-box;margin:0;padding:0}
html,body{width:1200px;height:1100px;overflow:hidden}
body{background:var(--page);font-family:Arimo,Arial,sans-serif;color:var(--ink);position:relative}
.abs{position:absolute}
a{color:var(--blue)}

/* header */
.site-header{left:100px;top:0;width:1000px;height:118px;background:var(--header)}
.brand{left:27px;top:26px;display:flex;align-items:center;gap:12px}
.brand-square{width:52px;height:52px;background:var(--blue)}
.brand-name{font-family:"PT Sans",sans-serif;font-size:64px;color:var(--blue);letter-spacing:-1px;line-height:1}
.tagline{right:32px;top:33px;text-align:right;font-size:11.5px;letter-spacing:4.2px;color:#9a9a9c;line-height:20px}

/* nav */
.main-nav{left:100px;top:117px;width:1000px;height:36px;background:linear-gradient(#fdfdfd,#d9d9d9);border-radius:0 0 4px 4px;display:flex}
.main-nav span{display:flex;align-items:center;justify-content:center;font-size:11px;letter-spacing:1px;color:#222;border-right:1px solid #bdbdbd;height:100%}

/* hero */
.hero-frame{left:127px;top:160px;width:688px;height:297px;background:#dcdcdc}
.hero-image{left:136px;top:169px;width:669px;height:279px;background:linear-gradient(100deg,#0d1f3f 0%,#123a72 40%,#2f74c4 65%,#9bb6d6 85%,#d9dde3 100%)}
.slide-tab{left:100px;width:27px;height:37px;background:var(--darker);color:#fff;font-family:"PT Sans",serif;font-style:italic;font-size:15px;display:flex;align-items:center;justify-content:center}
.slide-tab.active{background:var(--blue);width:278px;justify-content:flex-start;padding-left:7px}
.slide-tab.active b{font-style:normal;font-weight:400;font-family:Arimo,Arial,sans-serif;font-size:17px;margin-left:32px}
.slide-caption{left:136px;top:247px;width:242px;height:136px;background:rgba(6,10,20,.92);color:#ddd;font-size:11px;line-height:18px;padding:19px 8px 0 8px;text-align:justify}
.slide-caption a{position:absolute;right:20px;bottom:30px;color:#3d8bd8}

/* right column */
.login-bar{left:821px;top:154px;width:271px;height:39px;background:var(--dark);border-radius:0 0 4px 4px}
.login-label{left:8px;top:12px;font-size:10px;letter-spacing:1px;color:#ccc;display:flex;align-items:flex-end;gap:3px}
.search{left:109px;top:8px;width:127px;height:22px;background:#2d2e30;color:#999;font-size:10px;letter-spacing:1px;padding:5px 6px}
.search-btn{left:236px;top:8px;width:24px;height:22px;background:#3a3b3d}
.news{left:821px;top:201px;width:251px;height:183px;background:var(--panel);border-radius:4px}
.news h2{position:absolute;left:15px;top:9px;font-family:"PT Sans",sans-serif;font-weight:400;font-size:19px;color:var(--blue)}
.news-rule{left:0;top:34px;width:251px;height:1px;background:#fff}
.news-item{left:17px;width:213px;font-size:11px;line-height:18px;color:#555;text-align:justify}
.news-item span{color:var(--blue);padding-left:2px}
.news-sep{left:15px;top:103px;width:224px;border-top:1px dotted #999}
.news-arrow{left:1072px;width:28px;height:34px;display:flex;align-items:center;justify-content:center}
.newsletter{left:821px;top:391px;width:271px;height:72px;background:var(--dark);border-radius:4px 4px 0 0}
.newsletter h2{position:absolute;left:17px;top:11px;font-family:"PT Sans",sans-serif;font-weight:400;font-size:18px;color:#fff}
.nl-field{left:21px;top:39px;width:199px;height:22px;background:#2d2e30;color:#888;font-size:10px;letter-spacing:1px;padding:5px 5px}
.btn{background:var(--blue);color:#fff;font-size:10px;letter-spacing:1px;display:flex;align-items:center;justify-content:center}

/* services */
.services{left:100px;top:464px;width:1000px;height:137px;background:var(--panel);border-radius:4px 4px 0 0;display:flex}
.service{position:relative;height:100%;border-right:1px solid #d8d8d8}
.service:last-child{border-right:0}
.service-icon{position:absolute;top:26px;width:86px;height:74px;border-radius:6px}
.service h3{position:absolute;top:20px;font-family:"PT Sans",sans-serif;font-weight:400;font-size:22px;color:var(--blue);white-space:nowrap}
.service p{position:absolute;top:57px;font-size:11px;line-height:18px;color:#555;text-align:justify}
.service a{position:absolute;top:115px;font-size:11px}

/* welcome */
.welcome{left:100px;top:600px;width:680px;height:283px;background:#fff}
.welcome h1{position:absolute;left:27px;top:22px;font-family:"PT Sans",sans-serif;font-weight:400;font-size:22px;color:#333}
.welcome-body{left:58px;top:67px;width:560px;font-size:11px;line-height:13px;color:#444}
.welcome-body p{margin-bottom:13px;text-align:justify}
.welcome-body ul{list-style:none;margin:0 0 14px 12px}
.welcome a.more{position:absolute;left:595px;top:232px;font-size:11px}

/* contact */
.contact{left:780px;top:600px;width:320px;height:283px;background:linear-gradient(90deg,#dcdcdc,#f6f6f6 18%,#fff)}
.contact h2{position:absolute;left:34px;top:24px;font-family:"PT Sans",sans-serif;font-weight:400;font-size:18px;color:#222}
.office-tab{top:56px;width:116px;height:24px;font-size:12px;color:#fff;padding:5px 8px}
.office-tab.active{background:var(--blue)}
.office-tab.idle{background:#3b3d40}
.address{left:47px;top:103px;font-size:12px;line-height:18px;color:#444;letter-spacing:.3px}
.contact-map{left:80px;top:178px;width:186px;height:92px;background:radial-gradient(ellipse at center,#c8c8c8 0%,#e6e6e6 60%,rgba(255,255,255,0) 100%)}
.map-link{left:35px;top:215px;font-size:11px;color:#555;letter-spacing:.3px}

/* footer */
.divider{top:897px;height:170px;border-left:1px dashed #aaa}
.footer-title{font-family:"PT Sans",sans-serif;font-size:18px;color:#fff}
.getintouch{left:119px;top:900px;font-size:11px;line-height:24px;color:#fff}
.getintouch .label{color:var(--yellow)}
.getintouch .office{font-size:12px;font-weight:700}
.field{background:var(--field);border:1px solid #2a2b2d;color:#888;font-size:10px;letter-spacing:.6px;padding:6px 4px}
.legal{left:788px;top:903px;font-size:11px;color:#eee}
.footer-brand{left:900px;top:950px;font-family:"PT Sans",sans-serif;font-size:22px;color:#9ea3a8}
</style>
</head>
<body>

<header class="site-header abs">
  <div class="brand abs"><span class="brand-square"></span><span class="brand-name">Corvantel</span></div>
  <div class="tagline abs">ACCOUNTING AND TAX<br>AUDIT AND ASSURANCE<br>SELF MANAGED SUPER</div>
</header>

<nav class="main-nav abs">
  <span style="width:157px">HOME</span>
  <span style="width:145px">ABOUT US</span>
  <span style="width:127px">HISTORY</span>
  <span style="width:120px">VALUES</span>
  <span style="width:148px">OUR SERVICES</span>
  <span style="width:114px">PEOPLE</span>
  <span style="width:189px;border-right:0">COMMUNITY</span>
</nav>

<section class="hero">
  <div class="hero-frame abs"></div>
  <div class="hero-image abs" role="img" aria-label="Photo of a pen pointing at a blue financial market chart"></div>
  <div class="slide-tab abs" style="top:170px">1</div>
  <div class="slide-tab active abs" style="top:210px">2<b>Accounting and Taxation</b></div>
  <div class="slide-tab abs" style="top:250px">3</div>
  <div class="slide-tab abs" style="top:290px">4</div>
  <div class="slide-caption abs">AG Corvantel Chartered Accountants - provide traditional accounting services and professional corporate and business advice.<a href="#">more</a></div>
</section>

<aside>
  <div class="login-bar abs">
    <div class="login-label abs">
      <svg width="16" height="18" viewBox="0 0 16 18"><rect x="7" y="1" width="9" height="8" rx="1" fill="#f0a81c"/><circle cx="6" cy="6" r="3.5" fill="#2f7dd1"/><path d="M0 17c0-5 3-7 6-7s6 2 6 7z" fill="#2f7dd1"/></svg>
      CLIENT LOGIN
    </div>
    <div class="search abs">SEARCH</div>
    <div class="search-btn abs"><svg width="24" height="22" viewBox="0 0 24 22"><circle cx="11" cy="10" r="3.5" fill="none" stroke="#ddd" stroke-width="1.6"/><path d="M13.5 12.5l3.5 3.5" stroke="#ddd" stroke-width="2"/></svg></div>
  </div>

  <div class="news abs">
    <h2>Latest News</h2>
    <div class="news-rule abs"></div>
    <div class="news-item abs" style="top:41px">Corvantel Super is a specialist division formed in July 2009 to specifically <span>Uploaded 07/03/2011</span> Governments</div>
    <div class="news-sep abs"></div>
    <div class="news-item abs" style="top:115px">Corvantel Super is a specialist division formed in July 2009 to specifically <span>Uploaded 07/03/2011</span> Governments</div>
  </div>
  <div class="news-arrow abs" style="top:207px;background:var(--blue)"><svg width="22" height="22" viewBox="0 0 22 22"><circle cx="11" cy="11" r="10" fill="#fff"/><path d="M11 17V6M6 10l5-5 5 5" stroke="#1a1a1a" stroke-width="2.4" fill="none"/></svg></div>
  <div class="news-arrow abs" style="top:241px;background:var(--darker)"><svg width="22" height="22" viewBox="0 0 22 22"><circle cx="11" cy="11" r="10" fill="#888"/><path d="M11 5v11M6 12l5 5 5-5" stroke="#1a1a1a" stroke-width="2.4" fill="none"/></svg></div>

  <div class="newsletter abs">
    <h2>Subscribe Newsletter</h2>
    <div class="nl-field abs">Email Address...</div>
    <div class="btn abs" style="left:220px;top:39px;width:36px;height:22px">SEND</div>
  </div>
</aside>

<section class="services abs">
  <div class="service" style="width:340px">
    <div class="service-icon" style="left:10px;background:linear-gradient(#7a4a25,#4a2a14)" role="img" aria-label="Brown leather briefcase"></div>
    <h3 style="left:101px">Accounting &amp; Advisory</h3>
    <p style="left:101px;width:225px">AG Corvantel Chartered Accountants - provide traditional accounting services and professional corporate and business advice.</p>
    <a href="#" style="left:285px">more</a>
  </div>
  <div class="service" style="width:344px">
    <div class="service-icon" style="left:10px;background:linear-gradient(#f2efe8,#8a5a35)" role="img" aria-label="Open planner with a pencil"></div>
    <h3 style="left:108px">Audit &amp; Assurance</h3>
    <p style="left:108px;width:225px">While the number of firms providing audit services has decreased in recent years, Corvantel remain committed to audit as a core</p>
    <a href="#" style="left:300px">more</a>
  </div>
  <div class="service" style="width:316px">
    <div class="service-icon" style="left:6px;width:50px;background:radial-gradient(circle at 50% 35%,#ffe27a,#f0a81c 55%,#9a9a9a 80%)" role="img" aria-label="Glowing light bulb"></div>
    <h3 style="left:63px">Self Managed Super Funds</h3>
    <p style="left:68px;width:225px">Corvantel Super is a specialist division formed in July 2009 to specifically service our rapidly growing SMSF client base, in response to the</p>
    <a href="#" style="left:270px">more</a>
  </div>
</section>

<main class="welcome abs">
  <h1>Welcome Corvantel Group</h1>
  <div class="welcome-body abs">
    <p>Corvantel is a Tasmanian based firm which offers the skills of Accountants, Business Performance Advisers, Auditors and Self Managed Super Fund Specialists.</p>
    <p>From our offices in Devonport and Hobart we deliver services across three divisions:</p>
    <ul>
      <li>* AG Corvantel Chartered Accountants</li>
      <li>* Corvantel Audit &amp; Assurance</li>
      <li>* Corvantel Super</li>
    </ul>
    <p>Through our three divisions, our clients benefit from the application of specialist skills and systems, developed in relevant areas of expertise. At the same time, our teams are skilled at integrating their knowledge with the common goal of meeting our clients' comprehensive needs.</p>
  </div>
  <a class="more" href="#">more</a>
</main>

<section class="contact abs">
  <h2>Contact Us</h2>
  <div class="office-tab active abs" style="left:27px">Devonport Office</div>
  <div class="office-tab idle abs" style="left:145px;left:145px">Hobart Office</div>
  <svg class="abs" style="left:69px;top:80px" width="18" height="12" viewBox="0 0 18 12"><path d="M0 0h18L9 12z" fill="#1a63a8"/></svg>
  <div class="address abs">Level 1, 27 Harlow Street,<br>Devonport PO Box 4172,<br>Devonport, TAS, 7315</div>
  <div class="contact-map abs" role="img" aria-label="Dotted world map"></div>
  <div class="map-link abs">click here for contact details</div>
</section>

<footer>
  <div class="getintouch abs">
    <div class="footer-title" style="margin-bottom:4px">Get in touch</div>
    <div class="office"><span class="label">Devonport Office</span> &nbsp;|&nbsp; Hobart Office</div>
    <div><span class="label">Phone</span> : 03 6110 2847</div>
    <div><span class="label">Fax</span> : 03 6110 2853</div>
    <div>info@corvantelgroup.com.au</div>
  </div>
  <div class="divider abs" style="left:329px"></div>

  <div class="footer-title abs" style="left:353px;top:898px">Send Message</div>
  <div class="field abs" style="left:355px;top:931px;width:170px;height:24px">Your Name</div>
  <div class="field abs" style="left:355px;top:963px;width:170px;height:24px">Your Business</div>
  <div class="field abs" style="left:355px;top:999px;width:170px;height:24px">Email Address</div>
  <div class="field abs" style="left:355px;top:1031px;width:170px;height:24px">Subject</div>
  <div class="field abs" style="left:539px;top:931px;width:211px;height:92px">Your Enquiry</div>
  <div class="btn abs" style="left:714px;top:1033px;width:35px;height:22px">SEND</div>

  <div class="divider abs" style="left:773px"></div>
  <div class="legal abs">All Rights Reserved © 2011 Corvantel Group | &nbsp;Privacy Policy</div>
  <div class="footer-brand abs">Corvantel</div>
</footer>

</body>
</html>
```